Rapidly Expanding Real Estate Firm Seeking Signage Designs for Multiple Properties

We would like a sign design template created that we can use at our apartment buildings. We would like a consistent sign appearance that is adaptable enough to be used at different locations, on different mediums, and in different sizes. All vary for signage depending on the local laws and regulations as well as the type and style of the property. But the sign design should be consistent enough to support our company's branding efforts; so people that see our sign know its our company but also that the specific property is unique. Our thought was to incorporate the property address; i.e. "418 Birch" along with a portion of our company logo(attached). Then tag our website address across the bottom. Or some combination of that structure/design. It may make sense to just use the address and website address across the bottom OR it might be good to say 418 Birch St in large font with "by Amber Ridge Holdings Group" underneath as sort of a tag line. Not quite sure.
But we definitely want the signage to be clearly visible, professional, and clean. Easily read for the street. Should be flexible enough to work on metal or wood or any other medium with updates for the address and maybe color.
This is not a for sale sign design request. The sign concept will be used at apartment buildings. Sample property photos are attached - we are looking for a design template that is flexible enough to work on various property types. Also could be wall mounted or a pylon sign. Concept should work either way.

Target Market(s)

Prospective Tenants 25-45 yrs of age with incomes ranging from $55k - $95k.

Industry/Entity Type

Real Estate - Apartments

Colors
59FF00
82FF00
B8FF75
E3FFCB
F4FFEA

Requirements
Must have
• The street address number, web address(www.amberridgeholdingsgroup.com), & incorporate our primary colors(green,white,black)
Nice to have
• "418 Birch St." by Amber Ridge
Should not have
• Should not say For Sale, For Lease, post our phone number.

```html
<!DOCTYPE html>
<html lang="en">
<head>
<meta charset="utf-8">
<title>418 Birch St. — Property Sign</title>
<link rel="stylesheet" href="https://fonts.googleapis.com/css2?family=Poppins:wght@500;600;700;800&display=swap">
<style>
  :root {
    --brand-green: #82c341;
    --sign-black: #1b1b1b;
    --slate-dark: #2c3a44;
    --slate-mid: #4a5d69;
    --slate-light: #6f8290;
    --white: #ffffff;
    --canvas-bg: #f2f2f2;
  }
  html, body {
    margin: 0;
    padding: 0;
    width: 1200px;
    height: 1200px;
    overflow: hidden;
    background: var(--canvas-bg);
  }
  .canvas {
    position: relative;
    width: 1200px;
    height: 1200px;
  }
  .property-sign {
    position: absolute;
    left: 280px;
    top: 60px;
    width: 640px;
    height: 1080px;
    box-shadow: 0 18px 40px rgba(0, 0, 0, 0.25);
    font-family: "Poppins", sans-serif;
  }
  .property-sign svg { display: block; width: 100%; height: 100%; }
  .brand-name { fill: var(--brand-green); font-weight: 700; }
  .address-number { fill: var(--brand-green); font-weight: 700; }
  .address-street { fill: var(--white); font-weight: 700; }
  .tagline-green { fill: var(--brand-green); font-weight: 600; }
  .tagline-white { fill: var(--white); font-weight: 600; }
  .web-address { fill: var(--white); font-weight: 500; }
</style>
</head>
<body>
<div class="canvas">
  <div class="property-sign">
    <svg viewBox="0 0 433 730" preserveAspectRatio="none" xmlns="http://www.w3.org/2000/svg">
      <defs>
        <linearGradient id="skylineTone" x1="0" y1="0" x2="1" y2="1">
          <stop offset="0" stop-color="var(--slate-light)"/>
          <stop offset="0.5" stop-color="var(--slate-mid)"/>
          <stop offset="1" stop-color="var(--slate-dark)"/>
        </linearGradient>
      </defs>

      <!-- backdrop photo area -->
      <rect class="skyline-photo" role="img" aria-label="Photo of glass high-rise towers seen from below"
            x="0" y="0" width="433" height="690" fill="url(#skylineTone)"/>

      <!-- green top corners forming the roof chevron -->
      <polygon class="roof-corner" points="0,0 217,0 0,178" fill="var(--brand-green)"/>
      <polygon class="roof-corner" points="217,0 433,0 433,178" fill="var(--brand-green)"/>

      <!-- black lower chevron panel -->
      <polygon class="address-panel" points="0,445 272,265 433,440 433,690 0,690" fill="var(--sign-black)"/>

      <!-- green accent slash -->
      <polygon class="accent-slash" points="50,288 108,288 0,372 0,328" fill="var(--brand-green)"/>

      <!-- white roof line -->
      <polygon class="roof-line" points="0,410 230,227 270,227 0,445" fill="var(--white)"/>

      <!-- brand name -->
      <text class="brand-name" x="217" y="174" text-anchor="middle" font-size="30" letter-spacing="1">AMBER RIDGE</text>
      <text class="brand-name" x="217" y="198" text-anchor="middle" font-size="13" letter-spacing="2.5">HOLDINGS GROUP LLC</text>

      <!-- address -->
      <text class="address-number" x="217" y="477" text-anchor="middle" font-size="72">418</text>
      <text class="address-street" x="217" y="546" text-anchor="middle" font-size="60" letter-spacing="-1">BIRCH ST.</text>

      <!-- tagline -->
      <text class="tagline-green" x="217" y="614" text-anchor="middle" font-size="23">BY</text>
      <text class="tagline-green" x="217" y="639" text-anchor="middle" font-size="23">AMBER RIDGE</text>
      <text class="tagline-white" x="217" y="664" text-anchor="middle" font-size="23">HOLDINGS GROUP</text>

      <!-- website band -->
      <rect class="web-band" x="0" y="686" width="433" height="44" fill="var(--brand-green)"/>
      <text class="web-address" x="217" y="713" text-anchor="middle" font-size="14.5">www.amberridgeholdingsgroupllc.com</text>
    </svg>
  </div>
</div>
</body>
</html>
```